occupational hygiene card design

We supply a service to the resource sector, commercial or government organisations to access health risks from physical or chemical hazards. We are a technical discipline that works within legislation.

Industry/Entity Type

Government

Contact Information for Business Card

KPLA
Kestrel plains occupational hygiene

```html
<!DOCTYPE html>
<html lang="en">
<head>
<meta charset="utf-8">
<title>KPLA Business Card</title>
<link rel="stylesheet" href="https://fonts.googleapis.com/css2?family=Oswald:wght@400;700&family=Roboto+Condensed:wght@400&display=swap">
<style>
  :root {
    --page: #ecebe8;
    --navy: #1f1f96;
    --navy-deep: #17177a;
    --navy-mark: #25259a;
    --green-dark: #17762f;
    --green-light: #6cc52b;
    --white: #ffffff;
    --faint-mark: #4a4ae6;
  }
  html, body {
    margin: 0;
    width: 1200px;
    height: 1024px;
    overflow: hidden;
    background: var(--page);
  }
  .canvas {
    position: relative;
    width: 1200px;
    height: 1024px;
  }
  .card {
    position: absolute;
    left: 180px;
    width: 840px;
    height: 480px;
    overflow: hidden;
    box-shadow: 0 8px 24px rgba(0,0,0,0.18);
  }
  .card--front { top: 24px; background: var(--navy); }
  .card--back {
    top: 524px;
    background: radial-gradient(ellipse at 55% 45%, #2626a4 0%, var(--navy) 55%, var(--navy-deep) 100%);
  }
  .card__shapes { position: absolute; inset: 0; }

  .brand { position: absolute; left: 48px; top: 150px; }
  .brand__name {
    font-family: "Oswald", sans-serif;
    font-weight: 700;
    font-size: 96px;
    line-height: 1;
    color: var(--navy-mark);
    letter-spacing: 2px;
  }
  .brand__tagline {
    margin-top: 6px;
    font-family: "Roboto Condensed", sans-serif;
    font-size: 13px;
    letter-spacing: 2px;
    text-transform: uppercase;
    color: var(--navy-mark);
  }

  .contact {
    position: absolute;
    right: 40px;
    top: 40px;
    font-family: "Roboto Condensed", sans-serif;
    font-size: 18px;
    color: var(--white);
    text-align: right;
  }
  .contact__line {
    display: flex;
    justify-content: flex-end;
    align-items: center;
    gap: 12px;
    height: 30px;
  }
  .contact__icon { width: 16px; height: 16px; }

  .person {
    position: absolute;
    left: 470px;
    top: 350px;
    font-family: "Oswald", sans-serif;
  }
  .person__name { font-size: 40px; color: var(--white); line-height: 1.1; }
  .person__role { font-size: 22px; color: var(--green-light); }

  .back-mark {
    position: absolute;
    left: 0; right: 0; top: 120px;
    text-align: center;
  }
  .back-mark__name {
    font-family: "Oswald", sans-serif;
    font-weight: 700;
    font-size: 180px;
    line-height: 1;
    color: var(--faint-mark);
    letter-spacing: 6px;
  }
  .back-mark__tagline {
    margin-top: 8px;
    font-family: "Roboto Condensed", sans-serif;
    font-size: 18px;
    letter-spacing: 5px;
    text-transform: uppercase;
    color: var(--faint-mark);
  }
</style>
</head>
<body>
<div class="canvas">

  <section class="card card--front" aria-label="Business card front">
    <svg class="card__shapes" width="840" height="480" viewBox="0 0 840 480">
      <path transform="translate(44 0)" fill="var(--green-dark)" d="M0 0 H520 C430 60 430 200 330 300 C260 370 200 420 180 480 H0 Z"/>
      <path transform="translate(30 0)" fill="var(--white)" d="M0 0 H520 C430 60 430 200 330 300 C260 370 200 420 180 480 H0 Z"/>
      <path transform="translate(20 0)" fill="var(--green-light)" d="M0 0 H520 C430 60 430 200 330 300 C260 370 200 420 180 480 H0 Z"/>
      <path transform="translate(10 0)" fill="var(--white)" d="M0 0 H520 C430 60 430 200 330 300 C260 370 200 420 180 480 H0 Z"/>
      <path fill="var(--white)" d="M0 0 H520 C430 60 430 200 330 300 C260 370 200 420 180 480 H0 Z"/>
    </svg>

    <div class="brand">
      <div class="brand__name">KPLA</div>
      <div class="brand__tagline">Kestrel plains occupational hygiene</div>
    </div>

    <div class="contact">
      <div class="contact__line">
        <span>0412345678901</span>
        <svg class="contact__icon" viewBox="0 0 16 16"><path fill="var(--green-light)" d="M3 1l3 3-2 2c1 2 3 4 5 5l2-2 3 3-2 3C7 15 1 9 1 3z"/></svg>
      </div>
      <div class="contact__line">
        <span>maren.holt@kpla.com.au</span>
        <svg class="contact__icon" viewBox="0 0 16 16"><rect x="1" y="3" width="14" height="10" fill="var(--green-light)"/><path d="M1 3l7 6 7-6" fill="none" stroke="var(--navy)" stroke-width="1.5"/></svg>
      </div>
      <div class="contact__line">
        <span>www.kpla.com.au</span>
        <svg class="contact__icon" viewBox="0 0 16 16"><circle cx="8" cy="8" r="7" fill="var(--green-light)"/><path d="M1 8h14M8 1v14M3 4c3 1.5 7 1.5 10 0M3 12c3-1.5 7-1.5 10 0" fill="none" stroke="var(--navy)" stroke-width="1"/></svg>
      </div>
    </div>

    <div class="person">
      <div class="person__name">Maren Holt</div>
      <div class="person__role">Managing Director</div>
    </div>
  </section>

  <section class="card card--back" aria-label="Business card back">
    <div class="back-mark">
      <div class="back-mark__name">KPLA</div>
      <div class="back-mark__tagline">Kestrel plains occupational hygiene</div>
    </div>
  </section>

</div>
</body>
</html>
```